Window Graphic - Restaurant Interior

We are looking to have designed a Window Graphic created to promote our dinner and pita combos in store. the graphic will be applied to the front side of our counter area glass Dimensions are 18"H x 131" LONG (FRONT) AND THE 2 SIDES ARE 18" H X 16" LONG (LEFT AND RIGHT) - SEE ATTACHED IMAGES OF THE GLASS AREA.

Our 4 Family Combos have also been attached.

PANTONE 306U (BLUE)

Target Market(s)

WOMEN AGES 18-45

Industry/Entity Type

Greek Restaurant

Font styles to use
Serif

Colors
0392cd
0455a3
33a6d7

Requirements
Must have
• Images of Food, The 4 combos, Logo (Bright Olive)

```html
<!DOCTYPE html>
<html lang="en">
<head>
<meta charset="utf-8">
<title>Bright Olive – Family Combos Counter Graphic</title>
<link href="https://fonts.googleapis.com/css2?family=Teko:wght@500&family=Fira+Sans+Condensed:wght@400;600&family=Montserrat:wght@800&display=swap" rel="stylesheet">
<style>
  :root {
    --sky: #22b5e2;
    --navy: #1d3a4c;
    --white: #ffffff;
    --note: #2f5f78;
    --plate: #e9eef1;
    --food-warm: #b98a5a;
    --food-green: #7fae5a;
  }
  html, body { margin: 0; padding: 0; overflow: hidden; }
  body { width: 1200px; height: 165px; background: var(--sky); }
  .banner { position: relative; width: 1200px; height: 165px; background: var(--sky); overflow: hidden; }

  .combo { position: absolute; top: 0; height: 165px; }
  .combo__photo { position: absolute; border-radius: 50%; }
  .combo__photo--pita { background: radial-gradient(ellipse at 55% 45%, #c9ccd0 0%, #d8b08a 30%, var(--plate) 62%); }
  .combo__photo--dinner { background: radial-gradient(ellipse at 50% 50%, var(--food-warm) 0%, #d9c07a 28%, var(--food-green) 45%, var(--plate) 66%); }

  .combo__title {
    position: absolute; right: 0; top: 6px; margin: 0;
    font-family: "Teko", "Oswald", sans-serif; font-weight: 500;
    font-size: 44px; line-height: 1; color: var(--navy); letter-spacing: 0.5px;
    white-space: nowrap; text-transform: uppercase;
  }
  .combo__for {
    position: absolute; right: 0; top: 41px;
    font-family: "Teko", "Oswald", sans-serif; font-weight: 500;
    font-size: 15px; line-height: 1; color: var(--navy); text-transform: uppercase;
  }
  .combo__price {
    position: absolute; right: 0; top: 54px; width: 100px; height: 34px;
    border: 1.5px dashed var(--white); border-right-style: dashed;
    box-sizing: border-box; display: flex; align-items: center; justify-content: center;
    font-family: "Montserrat", sans-serif; font-weight: 800; color: var(--white);
    font-size: 29px; line-height: 1;
  }
  .combo__price .cur { font-size: 14px; align-self: flex-start; margin-top: 4px; margin-right: 2px; }
  .combo__price .cents { font-size: 14px; align-self: flex-start; margin-top: 4px; margin-left: 1px; }

  .combo__desc {
    position: absolute; margin: 0;
    font-family: "Fira Sans Condensed", sans-serif; font-weight: 600;
    font-size: 9.5px; line-height: 1.35; color: var(--navy);
  }
  .combo__note {
    position: absolute; margin: 0; white-space: nowrap;
    font-family: "Fira Sans Condensed", sans-serif; font-weight: 400;
    font-size: 7px; color: var(--note);
  }

  .brand {
    position: absolute; left: 527px; top: 35px; width: 94px; height: 94px;
    border-radius: 50%; background: var(--white);
    display: flex; align-items: center; justify-content: center; text-align: center;
  }
  .brand__name {
    font-family: "Teko", "Oswald", sans-serif; font-weight: 500;
    font-size: 24px; line-height: 0.9; color: var(--sky); text-transform: uppercase;
  }
</style>
</head>
<body>
<main class="banner">

  <section class="combo" style="left:0; width:236px;">
    <div class="combo__photo combo__photo--pita" role="img" aria-label="Foil-wrapped gyro pita sandwich on a white plate" style="left:28px; top:40px; width:138px; height:82px;"></div>
    <h2 class="combo__title">Pita Combo</h2>
    <span class="combo__for">For 2</span>
    <div class="combo__price"><span class="cur">$</span>22<span class="cents">95</span></div>
    <p class="combo__desc" style="left:32px; top:131px; width:210px;">Choice of any 2 Pita Sandwiches with choice of fries or salads &amp; 2 cans of pop.</p>
  </section>

  <section class="combo" style="left:248px; width:232px;">
    <div class="combo__photo combo__photo--pita" role="img" aria-label="Open pita wrap with meat, lettuce and tomato on a white plate" style="left:24px; top:42px; width:130px; height:78px;"></div>
    <h2 class="combo__title">Pita Combo</h2>
    <span class="combo__for">For 4</span>
    <div class="combo__price"><span class="cur">$</span>42<span class="cents">95</span></div>
    <p class="combo__desc" style="left:32px; top:131px; width:210px;">Choice of any 4 Pita Sandwiches with choice of fries or salads &amp; 4 cans of pop.</p>
  </section>

  <div class="brand"><span class="brand__name">Bright<br>Olive</span></div>

  <section class="combo" style="left:660px; width:242px;">
    <div class="combo__photo combo__photo--dinner" role="img" aria-label="Dinner plate with skewer, rice, roasted potatoes, greek salad and tzatziki" style="left:12px; top:36px; width:130px; height:84px;"></div>
    <h2 class="combo__title">Dinner Combo</h2>
    <span class="combo__for">For 2</span>
    <div class="combo__price"><span class="cur">$</span>26<span class="cents">95</span></div>
    <p class="combo__desc" style="left:148px; top:106px; width:100px;">Choice of any 2 Dinners with 2 cans of pop.</p>
    <p class="combo__note" style="left:30px; top:137px;">Dinners includes greek salad, rice, lemon roasted potatoes &amp; Tzatziki.</p>
  </section>

  <section class="combo" style="left:922px; width:242px;">
    <div class="combo__photo combo__photo--dinner" role="img" aria-label="Dinner plate with sliced gyro meat, rice, roasted potatoes, greek salad and tzatziki" style="left:2px; top:36px; width:140px; height:86px;"></div>
    <h2 class="combo__title">Dinner Combo</h2>
    <span class="combo__for">For 4</span>
    <div class="combo__price"><span class="cur">$</span>52<span class="cents">95</span></div>
    <p class="combo__desc" style="left:148px; top:106px; width:100px;">Choice of any 4 Dinners with 4 cans of pop.</p>
    <p class="combo__note" style="left:30px; top:137px;">Dinners includes greek salad, rice, lemon roasted potatoes &amp; Tzatziki.</p>
  </section>

</main>
</body>
</html>
```